Bright Parcel is a blog featuring products that give back. Products with a conscience.

The style of the blog should be STYLISH, Clean CHIC lines.
Color's to be used Grey & yellow or
Grey & navy blue.

examples/style references:

http://pantryloft.example/provisions (this one is my favorite)

http://mindfulvane.example/portfolio/commerce-home-facelift/

http://www.korvadine.example

Attached are style references as a guidelines.

It is time to create an alternative form of raising cash for good, other than traditional fundraising.

You proceeds go towards "Project based" causes. For example- helping feed children a lunch meal via the Tiffinrow fund.

The blog will feature-Special Limited Edition partnerships/collaborations with brands like ZUT will donate 100 percent of the proceeds to specific charities.

There will be a social component- where sharing it on your social media is essential. For example- I can post my purchase of jeans from Marrow on my Chatterly and the cause I helped. "Check out my new jeans & it's super amazing that I fed a child a lunch meal at the same time". Nominate your friends to do the same.

```html
<!DOCTYPE html>
<html lang="en">
<head>
<meta charset="utf-8">
<title>Bright Parcel</title>
<link href="https://fonts.googleapis.com/css2?family=Jost:wght@400&family=Open+Sans:wght@400;600&family=Great+Vibes&display=swap" rel="stylesheet">
<style>
  :root {
    --ink: #1a1a1a;
    --text: #555;
    --nav-active: #1a5eb0;
    --sun: #fedd3c;
    --royal: #0a4fa3;
    --footer: #0a52a6;
    --teal: #1f8d8a;
    --line: #e3e3e3;
    --script: #2a5fb0;
  }
  * { box-sizing: border-box; margin: 0; padding: 0; }
  html, body { width: 1083px; height: 1200px; overflow: hidden; background: #fff; }
  body { position: relative; font-family: "Open Sans", sans-serif; color: var(--ink); }
  .abs { position: absolute; }

  .brand { left: 114px; top: 32px; font-family: "Jost", sans-serif; font-size: 25px; letter-spacing: 1.5px; color: var(--ink); }
  .nav { left: 585px; top: 37px; display: flex; gap: 27px; font-size: 13px; }
  .nav a { color: var(--ink); text-decoration: none; }
  .nav a.active { color: var(--nav-active); }
  .social { display: flex; gap: 6px; }
  .social svg { width: 24px; height: 22px; }
  .header-social { left: 864px; top: 34px; }

  .hero-photo { left: 114px; top: 88px; width: 658px; height: 410px; background: linear-gradient(110deg, #d98aa6 0%, #c97a8a 35%, #e6c7a8 60%, #3a3a3a 100%); }
  .hero-panel { left: 772px; top: 88px; width: 198px; height: 410px; background: var(--sun); }
  .hero-date { left: 795px; top: 174px; width: 145px; border-top: 1px dashed #a08a20; border-bottom: 1px dashed #a08a20; padding: 4px 3px; font-size: 9.5px; color: #6b5c14; }
  .hero-title { left: 794px; top: 205px; width: 170px; font-size: 21px; line-height: 24px; color: #222; }
  .hero-text { left: 795px; top: 259px; width: 150px; font-size: 12.5px; line-height: 14.5px; color: #222; }
  .hero-btn { left: 795px; top: 334px; width: 124px; height: 29px; background: var(--royal); color: #fff; font-size: 13px; font-weight: 600; display: flex; align-items: center; justify-content: center; }
  .hero-thumbs { left: 795px; top: 385px; display: flex; gap: 2px; }
  .hero-thumbs div { width: 47px; height: 47px; }
  .arrow { width: 16px; height: 24px; }
  .arrow-prev { left: 84px; top: 265px; }
  .arrow-next { left: 980px; top: 285px; }

  .welcome { left: 0; top: 550px; width: 1083px; text-align: center; font-family: "Jost", sans-serif; font-size: 37px; letter-spacing: .5px; }
  .intro { left: 220px; top: 602px; width: 643px; text-align: center; font-size: 11.3px; line-height: 14px; color: var(--text); }

  .card { top: 659px; width: 210px; height: 309px; border: 1px solid var(--line); }
  .card-photo { width: 100%; height: 167px; position: relative; }
  .card-meta { position: absolute; left: 0; bottom: 0; width: 100%; height: 32px; background: rgba(255,255,255,.7); display: flex; justify-content: space-between; align-items: center; padding: 0 14px 0 16px; font-size: 10px; font-style: italic; }
  .card-meta span { display: flex; align-items: center; gap: 4px; }
  .card-title { margin: 22px 0 0 16px; font-size: 14px; line-height: 17px; width: 180px; }
  .card-more { margin: 10px 0 0 17px; font-family: "Great Vibes", cursive; font-size: 18px; color: #999; }
  .card-more.lead { color: var(--script); }
  .card-share { margin: 12px 0 0 16px; display: flex; gap: 4px; font-size: 8px; color: #333; }
  .card-share span { border: 1px solid #ccc; border-radius: 2px; padding: 1px 4px; background: #f6f6f6; }

  .footer { left: 0; top: 1017px; width: 1083px; height: 181px; background: var(--footer); color: #fff; }
  .f-head { top: 1051px; font-family: "Jost", sans-serif; font-size: 15px; color: #e8eef8; }
  .f-list { top: 1082px; list-style: none; font-size: 10px; line-height: 16.2px; }
  .f-list li::before { content: "\25B8"; font-size: 7px; margin-right: 3px; vertical-align: 1px; }
  .gallery { left: 444px; top: 1084px; display: grid; grid-template-columns: repeat(3, 45px); gap: 6px 5px; }
  .gallery div { height: 38px; background: linear-gradient(135deg, #b87a8c, #5b4a50); }
  .email { left: 634px; top: 1083px; width: 114px; height: 23px; background: #fff; color: #888; font-size: 10px; padding: 5px 8px; }
  .subscribe { left: 748px; top: 1083px; width: 73px; height: 23px; background: var(--teal); font-size: 11.5px; display: flex; align-items: center; justify-content: center; }
  .footer-social { left: 864px; top: 1079px; }
  .copy { left: 868px; top: 1117px; font-size: 10px; }
</style>
</head>
<body>
  <svg width="0" height="0" style="position:absolute">
    <defs>
      <symbol id="heart" viewBox="0 0 24 22">
        <path d="M12 20.5 C5 15 1.5 11.5 1.5 6.8 A5 5 0 0 1 12 4.8 A5 5 0 0 1 22.5 6.8 C22.5 11.5 19 15 12 20.5 Z" fill="none" stroke="currentColor" stroke-width="1.4"/>
      </symbol>
    </defs>
  </svg>

  <header>
    <div class="abs brand">BRIGHT PARCEL</div>
    <nav class="abs nav">
      <a class="active" href="#">HOME</a>
      <a href="#">RECENT ARTICALS</a>
      <a href="#">CONTACT</a>
    </nav>
    <div class="abs social header-social" style="color:#666">
      <svg role="img" aria-label="Chatterly"><use href="#heart"/></svg>
      <svg role="img" aria-label="Chirpline"><use href="#heart"/></svg>
      <svg role="img" aria-label="Feed"><use href="#heart"/></svg>
      <svg role="img" aria-label="Professional network"><use href="#heart"/></svg>
    </div>
  </header>

  <section class="hero">
    <svg class="abs arrow arrow-prev" viewBox="0 0 16 24"><path d="M12 3 L4 12 L12 21" fill="none" stroke="#666" stroke-width="3"/></svg>
    <div class="abs hero-photo" role="img" aria-label="Smiling girl with a school bag and her mother beside a school bus"></div>
    <div class="abs hero-panel"></div>
    <div class="abs hero-date">April 16, 2014,</div>
    <h2 class="abs hero-title" style="font-weight:400">Lorem Ipsum donor sid amet</h2>
    <p class="abs hero-text">Explain implementation of a lottery and select applicants and keep you out of that process</p>
    <div class="abs hero-btn">LEARN MORE</div>
    <div class="abs hero-thumbs">
      <div role="img" aria-label="Child eating lunch" style="background:#6b4a4a"></div>
      <div role="img" aria-label="Girl with school bag" style="background:#c98aa6;outline:1px solid #fff"></div>
      <div role="img" aria-label="Lunch box with snacks" style="background:#3d4a35"></div>
    </div>
    <svg class="abs arrow arrow-next" viewBox="0 0 16 24"><path d="M4 3 L12 12 L4 21" fill="none" stroke="#666" stroke-width="3"/></svg>
  </section>

  <section class="posts">
    <h1 class="abs welcome" style="font-weight:400">WELCOME TO BRIGHT PARCEL</h1>
    <p class="abs intro">Lorem ipsum dolor sit amet, consec tetur adipiscing elit. In fermentum dolor non augue pretium egestas. Donec tincidunt at congue ut, posuere sit amet est. Vivamus scelerisque pretium ...</p>

    <article class="abs card" style="left:115px">
      <div class="card-photo" role="img" aria-label="Lunch box with sushi rolls, blueberries and grapes" style="background:linear-gradient(135deg,#9acb4a,#c9c9c4 45%,#5b6660)">
        <div class="card-meta">April 16, 2014, <span>&#9679; 05</span></div>
      </div>
      <h3 class="card-title" style="font-weight:400">Donec tincidunt at congue posuere sit amet est..</h3>
      <div class="card-more lead">Read More</div>
      <div class="card-share"><span>Like</span><span>3k</span><span>Post</span><span>316</span></div>
    </article>

    <article class="abs card" style="left:330px">
      <div class="card-photo" role="img" aria-label="Two young children sitting outdoors with a drink" style="background:linear-gradient(135deg,#3f5a2c,#8a9a6a 50%,#c8662e)">
        <div class="card-meta">April 16, 2014, <span>&#9679; 05</span></div>
      </div>
      <h3 class="card-title" style="font-weight:400">Donec tincidunt at congue posuere sit amet est..</h3>
      <div class="card-more">Read More</div>
      <div class="card-share"><span>Like</span><span>3k</span><span>Post</span><span>316</span></div>
    </article>

    <article class="abs card" style="left:544px">
      <div class="card-photo" role="img" aria-label="Steel lunch tin with bread, greens and blueberries" style="background:linear-gradient(135deg,#7a4a2e,#b8b2a8 50%,#5a3a26)">
        <div class="card-meta">April 16, 2014, <span>&#9679; 05</span></div>
      </div>
      <h3 class="card-title" style="font-weight:400">Donec tincidunt at congue posuere sit amet est..</h3>
      <div class="card-more">Read More</div>
      <div class="card-share"><span>Like</span><span>3k</span><span>Post</span><span>316</span></div>
    </article>

    <article class="abs card" style="left:760px">
      <div class="card-photo" role="img" aria-label="Stack of colourful dotted lunch boxes" style="background:linear-gradient(135deg,#a9d84a,#f07a2a 40%,#2aa0e0 65%,#e83a7a)">
        <div class="card-meta">April 16, 2014, <span>&#9679; 05</span></div>
      </div>
      <h3 class="card-title" style="font-weight:400">Donec tincidunt at congue posuere sit amet est..</h3>
      <div class="card-more">Read More</div>
      <div class="card-share"><span>Like</span><span>3k</span><span>Post</span><span>316</span></div>
    </article>
  </section>

  <footer>
    <div class="abs footer"></div>
    <h4 class="abs f-head" style="left:114px;font-weight:400">BP Information</h4>
    <ul class="abs f-list" style="left:114px"><li>Home</li><li>About us</li><li>Recent Blogs</li><li>Latest News</li><li>Contact us</li></ul>
    <ul class="abs f-list" style="left:202px"><li>Lorem&nbsp; Name 1</li><li>Lorem&nbsp; Name 2</li><li>Lorem&nbsp; Name 3</li><li>Lorem&nbsp; Name 4</li><li>Lorem&nbsp; Name 5</li></ul>
    <ul class="abs f-list" style="left:302px"><li>Lorem&nbsp; Name 6</li><li>Lorem&nbsp; Name 7</li><li>Lorem&nbsp; Name 8</li><li>Lorem&nbsp; Name 9</li><li>Lorem&nbsp; Name 10</li></ul>

    <h4 class="abs f-head" style="left:442px;font-weight:400">Our Gallery</h4>
    <div class="abs gallery">
      <div role="img" aria-label="Gallery photo"></div><div role="img" aria-label="Gallery photo"></div><div role="img" aria-label="Gallery photo" style="background:linear-gradient(135deg,#3a8a3a,#2a2a2a)"></div>
      <div role="img" aria-label="Gallery photo"></div><div role="img" aria-label="Gallery photo"></div><div role="img" aria-label="Gallery photo"></div>
    </div>

    <h4 class="abs f-head" style="left:634px;font-weight:400">Newsletter Signup</h4>
    <div class="abs email">Email Id</div>
    <div class="abs subscribe">Subscribe</div>

    <h4 class="abs f-head" style="left:865px;font-weight:400">Our Location</h4>
    <div class="abs social footer-social" style="color:#fff">
      <svg role="img" aria-label="Chatterly"><use href="#heart"/></svg>
      <svg role="img" aria-label="Chirpline"><use href="#heart"/></svg>
      <svg role="img" aria-label="Feed"><use href="#heart"/></svg>
      <svg role="img" aria-label="Professional network"><use href="#heart"/></svg>
    </div>
    <div class="abs copy">&copy; 2014 / Terms of use</div>
  </footer>
</body>
</html>
```